Banner ad to sell prefabricated holiday homes in New Zealand

Harbor Nest Homes build prefabricated homes in a factory that are then transported by truck to their site. It's coming into summer here in New Zealand and many people will be thinking about the holidays and wishing they had a holiday home.

The design should communicate some of the following benefits of our homes:
- Full project management
- Great value for money
- Delivered complete with all interior & exterior fittings
- Quality construction in our controlled factory

The banner ad will be displayed on a popular weather website www.skyvanecast.co.nz
Size: 760px x 120px
Would like it to be animated if but the size must be below 60kb.

I'll upload some nice holiday destination photos for backgrounds & some pictures of our holiday home designs for you to use.
Our main company colors are bright blue (pantone 3005) and light grey/silver.

Updatefor brief:
I would like the animation to show different text so that it's not all squashed up on the one image.
For example have "Prefabricated Holiday Homes" on one image & then it fades/changes to next image with "Delivered complete with all interior & exterior fittings". Or something like that with nice background images or pictures of our houses.

```html
<!DOCTYPE html>
<html lang="en">
<head>
<meta charset="utf-8">
<title>Harbor Nest Homes – Banner Set</title>
<link href="https://fonts.googleapis.com/css2?family=Exo+2:wght@700&display=swap" rel="stylesheet">
<style>
  :root {
    --canvas: #ececec;
    --white: #ffffff;
    --blue-deep: #1160ab;
    --blue-mid: #3478bb;
    --blue-sky: #36a6d8;
    --sky-top: #8fbde8;
    --sky-pale: #dbe9f5;
    --grass: #6f9a45;
    --sand: #e6d9c4;
    --sea: #3b9fd0;
    --road: #8a8f92;
  }
  * { margin: 0; padding: 0; box-sizing: border-box; }
  html, body { width: 1200px; height: 1000px; overflow: hidden; }
  body { background: var(--canvas); position: relative; font-family: "Exo 2", sans-serif; }

  .banner {
    position: absolute;
    left: 184px;
    width: 792px;
    height: 125px;
    background: var(--white);
    box-shadow: 5px 6px 9px rgba(0,0,0,0.38);
    overflow: hidden;
  }
  .banner--management { top: 141px; }
  .banner--value { top: 319px; }
  .banner--delivered { top: 511px; }
  .banner--quality { top: 707px; }

  .message {
    position: absolute;
    left: 0; top: 0; height: 125px;
    display: flex;
    flex-direction: column;
    align-items: center;
    justify-content: center;
    color: var(--white);
    text-align: center;
  }
  .message__headline {
    font-weight: 700;
    font-size: 24px;
    line-height: 31px;
    letter-spacing: 0.3px;
  }
  .brand {
    display: flex;
    align-items: center;
    gap: 7px;
    margin-top: 12px;
    font-weight: 700;
    font-size: 16px;
    color: var(--white);
  }
  .brand__mark {
    width: 18px; height: 18px;
    background: var(--white);
  }
  .banner--delivered .brand,
  .banner--quality .brand { margin-top: 6px; }
  .banner--delivered .message__headline,
  .banner--quality .message__headline { margin-top: -6px; }

  .message--deep { background: var(--blue-deep); }
  .message--mid { background: var(--blue-mid); }
  .message--sky { background: var(--blue-sky); }

  .tile { position: absolute; }
  .tile--deep { background: var(--blue-deep); }
  .tile--mid { background: var(--blue-mid); }
  .tile--sky { background: var(--blue-sky); }

  .photo-house { background: linear-gradient(180deg, var(--sky-top) 0%, var(--sky-pale) 38%, #7b7f7a 55%, var(--grass) 85%); }
  .photo-deck { background: linear-gradient(180deg, #6f9fd4 0%, #e9eef2 45%, #b9a88c 62%, #8a6a4a 100%); }
  .photo-beach { background: linear-gradient(180deg, var(--sky-top) 0%, var(--sea) 40%, #f4f6f6 58%, var(--sand) 75%); }
  .photo-truck { background: linear-gradient(180deg, var(--sky-top) 0%, var(--sky-pale) 40%, #8b7f70 55%, var(--road) 80%, var(--grass) 100%); }
</style>
</head>
<body>

  <section class="banner banner--management">
    <div class="message message--deep" style="width:383px">
      <p class="message__headline">Full project management</p>
      <div class="brand"><span class="brand__mark"></span>Harbor Nest Homes</div>
    </div>
    <div class="tile tile--mid" style="left:392px;top:0;width:133px;height:44px"></div>
    <div class="tile photo-house" style="left:392px;top:51px;width:133px;height:74px" role="img" aria-label="Dark single-storey holiday home with mountains behind"></div>
    <div class="tile photo-deck" style="left:532px;top:0;width:84px;height:125px" role="img" aria-label="Wooden deck with outdoor chairs under a summer sky"></div>
    <div class="tile photo-house" style="left:624px;top:0;width:168px;height:87px" role="img" aria-label="Modern dark holiday home in a garden setting"></div>
    <div class="tile tile--sky" style="left:624px;top:92px;width:168px;height:33px"></div>
  </section>

  <section class="banner banner--value">
    <div class="message message--mid" style="width:346px">
      <p class="message__headline">Great value for money</p>
      <div class="brand"><span class="brand__mark"></span>Harbor Nest Homes</div>
    </div>
    <div class="tile photo-house" style="left:356px;top:0;width:157px;height:84px" role="img" aria-label="Grey holiday home with garden and mountain view"></div>
    <div class="tile tile--deep" style="left:356px;top:88px;width:157px;height:37px"></div>
    <div class="tile photo-truck" style="left:521px;top:0;width:143px;height:125px" role="img" aria-label="Truck transporting a prefabricated home"></div>
    <div class="tile tile--sky" style="left:672px;top:0;width:120px;height:27px"></div>
    <div class="tile photo-beach" style="left:672px;top:35px;width:120px;height:90px" role="img" aria-label="Sandy beach with waves and coastal cliffs"></div>
  </section>

  <section class="banner banner--delivered">
    <div class="message message--mid" style="width:418px">
      <p class="message__headline">Delivered complete with<br>all interior &amp; exterior fittings</p>
      <div class="brand"><span class="brand__mark"></span>Harbor Nest Homes</div>
    </div>
    <div class="tile tile--sky" style="left:426px;top:0;width:138px;height:47px"></div>
    <div class="tile photo-house" style="left:426px;top:54px;width:138px;height:71px" role="img" aria-label="Pale holiday cottage with lawn and mountains"></div>
    <div class="tile photo-truck" style="left:572px;top:0;width:119px;height:87px" role="img" aria-label="Truck carrying a home along a road"></div>
    <div class="tile tile--deep" style="left:572px;top:94px;width:119px;height:31px"></div>
    <div class="tile photo-beach" style="left:699px;top:0;width:93px;height:125px" role="img" aria-label="Beach with surf and rocky headland"></div>
  </section>

  <section class="banner banner--quality">
    <div class="message message--sky" style="width:392px">
      <p class="message__headline">Quality construction<br>in our controlled factory</p>
      <div class="brand"><span class="brand__mark"></span>Harbor Nest Homes</div>
    </div>
    <div class="tile photo-house" style="left:398px;top:0;width:148px;height:98px" role="img" aria-label="Modern holiday home with tussock garden"></div>
    <div class="tile tile--deep" style="left:398px;top:104px;width:148px;height:21px"></div>
    <div class="tile tile--deep" style="left:553px;top:0;width:89px;height:61px"></div>
    <div class="tile photo-beach" style="left:553px;top:69px;width:89px;height:56px" role="img" aria-label="Calm beach under a blue sky"></div>
    <div class="tile photo-house" style="left:648px;top:0;width:144px;height:76px" role="img" aria-label="Dark holiday home with deck among trees"></div>
    <div class="tile tile--mid" style="left:648px;top:83px;width:144px;height:42px"></div>
  </section>

</body>
</html>
```